Course flyer - evolutive design

We want to have a nice design for our course programm.
In fact we are school language, and our course programm change approximatively each 2 weeks§.
For that we need a design that we can modify each 2 weeks (only dates change ) by ourselves.
We used to have a classical design but we want to upgrade it with a modern and attractive design.
We can have 3 versions one for each city.
We have 3 offices: Tunis, Sousse & Sfax
Attached you can find old designs

Target Market(s)

students from 16 years old till retired people 76 years old

Industry/Entity Type

Education

Font styles to use
Sans Serif

Requirements
Must have
• clear timing for courses (date, days, timing)
• prices
• Adresse (each flyer has its own adress)
• phone Number
• Cool image
Should not have
• Racism
• Violence
• Too much stuff

```html
<!DOCTYPE html>
<html lang="fr">
<head>
<meta charset="utf-8">
<title>Cours d'allemand – Sousse – Mars Avril 2016</title>
<link href="https://fonts.googleapis.com/css2?family=Open+Sans:wght@400;600;700&family=Roboto+Condensed:wght@400;700&display=swap" rel="stylesheet">
<style>
  :root{
    --brown:#7b6656;
    --brown-dark:#5f4d40;
    --cream:#f3ebc3;
    --cream-light:#fcf8e6;
    --accent:#e2552b;
    --lime:#c9d11c;
    --text:#6a6a6a;
    --text-dark:#3a3a3a;
    --white:#ffffff;
  }
  *{margin:0;padding:0;box-sizing:border-box}
  html,body{width:848px;height:1200px;overflow:hidden;background:var(--cream-light)}
  .flyer{position:relative;width:848px;height:1200px;overflow:hidden;font-family:"Open Sans",Arial,sans-serif;color:var(--text)}
  .backdrop{position:absolute;inset:0}
  .headline{position:absolute;right:18px;top:30px;text-align:right;font-family:"Roboto Condensed",Arial,sans-serif;font-weight:700;color:var(--white);line-height:1}
  .headline .subject{font-size:47px;letter-spacing:.5px}
  .headline .months{font-size:66px;text-align:center;margin:14px 150px 0 0;line-height:.92}
  .headline .year{position:absolute;right:108px;top:208px;font-size:168px;color:var(--lime);letter-spacing:-2px}
  .city{position:absolute;left:-86px;top:540px;width:320px;transform:rotate(-90deg);font-size:104px;font-weight:400;color:var(--white);text-align:center;letter-spacing:-1px}
  .session{position:absolute}
  .session h2{font-size:21px;font-weight:700;color:var(--accent)}
  .session h2 small{font-size:17px;font-weight:600}
  .session .period{font-size:21px;font-weight:700;color:var(--text);margin-top:12px}
  .levels{display:grid;grid-template-columns:repeat(2,auto);justify-content:start;column-gap:40px;row-gap:4px;margin-top:16px;list-style:none}
  .levels.single{grid-template-columns:auto}
  .levels li{font-size:21px;font-weight:700;color:var(--text);white-space:nowrap}
  .levels li span{font-size:16px;font-weight:400;margin-left:8px}
  .levels.stacked{grid-auto-flow:column;grid-template-rows:repeat(4,auto)}
  .levels.stacked3{grid-auto-flow:column;grid-template-rows:repeat(3,auto)}
  .notes{position:absolute;left:235px;top:1000px;width:250px;font-size:10px;line-height:1.35;color:var(--text-dark)}
  .notes p{margin-bottom:6px}
  .brand{position:absolute;left:36px;top:930px;display:flex;align-items:center;gap:12px;font-family:"Open Sans",Arial,sans-serif;font-weight:700;font-size:58px;color:var(--text-dark);letter-spacing:-1px}
  .brand .dot{width:26px;height:26px;border-radius:50%;background:var(--lime)}
  .office{position:absolute;left:348px;top:1098px;font-size:13px;line-height:1.45;color:var(--text-dark)}
  .office strong{font-size:16px;font-weight:700}
  .contact{position:absolute;left:556px;top:1096px;list-style:none}
  .contact li{display:flex;align-items:center;gap:12px;font-size:15px;color:var(--text-dark);height:23px}
  .contact svg{width:18px;height:18px;fill:var(--brown-dark)}
</style>
</head>
<body>
<main class="flyer">
  <svg class="backdrop" width="848" height="1200" viewBox="0 0 848 1200">
    <defs>
      <linearGradient id="photoTone" x1="0" y1="0" x2="1" y2="1">
        <stop offset="0" stop-color="#3f6a2a"/>
        <stop offset=".45" stop-color="#8fa84a"/>
        <stop offset="1" stop-color="#d8c77a"/>
      </linearGradient>
      <linearGradient id="footerTone" x1="0" y1="0" x2="1" y2="0">
        <stop offset="0" stop-color="#c9b99b"/>
        <stop offset="1" stop-color="#f6eed3"/>
      </linearGradient>
    </defs>
    <rect class="photo" x="0" y="0" width="848" height="470" fill="url(#photoTone)" role="img" aria-label="Photo de jeunes étudiants souriants avec sacs à dos et cahiers dans un parc ensoleillé"/>
    <rect x="0" y="440" width="848" height="760" fill="var(--cream-light)"/>
    <rect x="142" y="440" width="328" height="415" fill="var(--cream)"/>
    <path d="M142 440 C142 445 160 432 470 430 L470 442 L142 442 Z" fill="var(--cream)"/>
    <path d="M0 150 C70 175 142 270 142 440 L142 760 C142 820 80 850 0 862 Z" fill="var(--brown)"/>
    <path d="M0 862 C80 850 142 820 142 760" fill="none" stroke="var(--white)" stroke-width="3"/>
    <rect x="470" y="855" width="378" height="228" fill="var(--cream-light)"/>
    <rect x="142" y="855" width="328" height="228" fill="#f7f0d1"/>
    <rect x="330" y="1083" width="518" height="117" fill="url(#footerTone)"/>
  </svg>

  <header class="headline">
    <div class="subject">COURS D'ALLEMAND</div>
    <div class="months">MARS<br>AVRIL</div>
    <div class="year">2016</div>
  </header>

  <div class="city">Sousse</div>

  <section class="session" style="left:157px;top:458px">
    <h2>Intensif <small>Lundi - Vendredi</small></h2>
    <p class="period">07/03/2016 - 25/03/2016</p>
    <ul class="levels stacked">
      <li>A1.1<span>DK2090</span></li>
      <li>A1.2<span>DK2091</span></li>
      <li>A2.1<span>DK2092</span></li>
      <li>A2.2<span>DK2093</span></li>
      <li>B1.1<span>DK2098</span></li>
      <li>B1.1<span>DK2099</span></li>
      <li>B2.1<span>DK2094</span></li>
    </ul>
  </section>

  <section class="session" style="left:157px;top:670px">
    <p class="period" style="margin-top:0">28/03/2016 - 15/04/2016</p>
    <ul class="levels stacked">
      <li>A1.1<span>DK2105</span></li>
      <li>A1.2<span>DK2106</span></li>
      <li>A2.1<span>DK2107</span></li>
      <li>A2.2<span>DK2108</span></li>
      <li>B1.1<span>DK2112</span></li>
      <li>B1.2<span>DK2113</span></li>
      <li>B2.1<span>DK2109</span></li>
    </ul>
  </section>

  <section class="session" style="left:492px;top:458px">
    <h2>Extensif <small>( 3 jour/semaine )</small></h2>
    <p class="period">28/03/2016 - 22/04/2016</p>
    <ul class="levels single">
      <li>A1.1<span>DK2121</span></li>
      <li>A1.2<span>DK2122</span></li>
      <li>A2.2<span>DK2124</span></li>
    </ul>
  </section>

  <section class="session" style="left:497px;top:650px">
    <h2>Extensif <small>( 2 jour/semaine )</small></h2>
    <p class="period">28/03/2016 - 05/05/2016</p>
    <ul class="levels stacked3">
      <li>A1.1<span>DK2115</span></li>
      <li>A1.2<span>DK2116</span></li>
      <li>A2.1<span>DK2117</span></li>
      <li>A2.2<span>DK2118</span></li>
      <li>B1.2<span>DK2119</span></li>
      <li>B1.2<span>DK2120</span></li>
    </ul>
  </section>

  <div class="brand"><span class="dot"></span>lingora</div>

  <div class="notes">
    <p>Toute inscription doit imperativement se faire au plus tard une semaine avant le debut des cours.</p>
    <p>Nombre minimum de 5 participants requis</p>
    <p>L'horaire des cours est susceptible detre modifie.<br>Prix par module 340 TND.</p>
  </div>

  <address class="office" style="font-style:normal">
    <strong>Sfax</strong><br>
    Avenue des Oliviers<br>
    Rue Habib Salem<br>
    Immeuble Yasmine<br>
    (5eme etage)
  </address>

  <ul class="contact">
    <li><svg viewBox="0 0 24 24"><path d="M6.6 10.8a15 15 0 0 0 6.6 6.6l2.2-2.2c.3-.3.7-.4 1-.2 1.1.4 2.3.6 3.6.6.6 0 1 .4 1 1V20c0 .6-.4 1-1 1A17 17 0 0 1 3 4c0-.6.4-1 1-1h3.5c.6 0 1 .4 1 1 0 1.3.2 2.5.6 3.6.1.3 0 .7-.2 1z"/></svg>+216 70 000 123</li>
    <li><svg viewBox="0 0 24 24"><path d="M2 5h20v14H2z M3 6l9 7 9-7" fill="none" stroke="#5f4d40" stroke-width="2"/></svg>contact-sfax@lingora.org</li>
    <li><svg viewBox="0 0 24 24"><circle cx="12" cy="12" r="9" fill="none" stroke="#5f4d40" stroke-width="2"/><path d="M3 12h18M12 3c3 3 3 15 0 18M12 3c-3 3-3 15 0 18" fill="none" stroke="#5f4d40" stroke-width="1.6"/></svg>www.lingora.org</li>
    <li><svg viewBox="0 0 24 24"><rect x="3" y="3" width="18" height="18" rx="2"/></svg>www.social.net/lingora</li>
  </ul>
</main>
</body>
</html>
```